Meadowlark Behavioral Partners, LLC Needs Modern Business Card Design.

We provide behavioral health services from western Kansas to eastern Kansas. There is an abundance of competition for the services we provide with our main competitor being larger and having significantly more financial resources; however, the quality of services we provide is greater and we have started to catch the attention of the State of Kansas. We had a great logo designed by PixelGuild - this will be used to build upon our brand. The logo (attached) should be used in the card development. We want something unique, modern, but also a card design that clearly states our name, contact info, provides the name and unqiue location of each clinician, etc. Rounded edges, or a unique size, just something that makes our business card stand out from others. I have also uploaded each clinician's name and their unique location and phone number.

Our idea is to have one side be black with our logo. Then, on the other side have business cards for each individual. Plus, we want one card that is "generic" with no specific clinician's name listed so that we can give clients an appointment card when they leave. Some clinicians have two locations - we're open to design and background color, but we have started going with branding colors of black, the yellow in the logo files attached, and sometimes a gray. Our new office has been decorated using this theme.

Target Market(s)

individuals and families in need of behavioral health services; potential professional referral sources; existing referral sources

Industry/Entity Type

Business

Contact Information for Business Card

I attached a Word doc that provides clinician names, credentials and location information specific to each individual.

Font styles to use
Serif

Colors
000000
fbed22
dbdbdb
9d9d9d
c3c3c3

Requirements
Must have
• 1) use of the company logo that has been attached; 2) a template that provides us space to individualize business cards for all of our clinicians; 3) should stick to the colors we are branding with: black, yellow from the logo file, maybe a gray shade and we're open to a suggestion on a shade of white.
Nice to have
• Group discussion culminated in the thought that one side would be black with just our logo - no clinician names, etc. A unique design - rounded edges, unique size, some catchy lay-out would be nice.
Should not have
• Must not be too busy. Should look "clean." The project should stick to branding colors: black, yellow (from the logo file), maybe a gray and shade of white.

```html
<!DOCTYPE html>
<html lang="en">
<head>
<meta charset="utf-8">
<title>Meadowlark Behavioral Partners — Business Card</title>
<link rel="stylesheet" href="https://fonts.googleapis.com/css2?family=Arvo:wght@400;700&family=Lato:wght@400;700&display=swap">
<style>
  :root {
    --ink: #000000;
    --card-black: #0b0b0b;
    --panel-black: #131313;
    --gold: #f7b92f;
    --gold-light: #fcca45;
    --gold-deep: #e9a51f;
    --paper: #ececec;
    --white: #ffffff;
    --serif: "Arvo", Georgia, serif;
    --sans: "Lato", Arial, sans-serif;
  }
  * { box-sizing: border-box; margin: 0; padding: 0; }
  html, body { width: 1200px; height: 750px; overflow: hidden; }
  body { background: var(--paper); font-family: var(--sans); }

  .canvas {
    position: relative;
    width: 1200px; height: 750px;
    display: flex; justify-content: center; align-items: center; gap: 70px;
  }

  .card {
    position: relative;
    width: 330px; height: 570px;
    background: var(--card-black);
    border-radius: 14px;
    overflow: hidden;
    box-shadow: 0 10px 26px rgba(0,0,0,0.18);
  }

  /* ---------- Front: clinician side ---------- */
  .card-front .header-band {
    position: absolute; inset: 0 0 auto 0; height: 140px;
  }
  .header-band svg { display: block; width: 100%; height: 100%; }

  .brand-mark {
    position: absolute; top: 26px; left: 0; right: 0;
    text-align: center; color: var(--ink); font-family: var(--serif); font-weight: 700;
  }
  .brand-mark .dot {
    display: block; width: 18px; height: 18px; margin: 0 auto 6px;
    border-radius: 50%; background: var(--ink);
  }
  .brand-mark .name-main { display: block; font-size: 19px; letter-spacing: 1.5px; line-height: 1.1; }
  .brand-mark .name-sub { display: block; font-size: 9.5px; letter-spacing: 0.6px; margin-top: 2px; }

  .clinician {
    position: absolute; top: 160px; left: 0; right: 0; text-align: center;
    color: var(--gold); font-family: var(--serif);
  }
  .clinician .person { font-size: 21px; font-weight: 400; letter-spacing: 0.5px; }
  .clinician .role { font-size: 14px; font-weight: 700; margin-top: 4px; }

  .contact-panel {
    position: absolute; top: 236px; left: 0; right: 0; height: 176px;
    background: var(--panel-black);
  }
  .icon-rail { position: absolute; top: -1px; left: 0; right: 0; height: 32px; }
  .icon-rail::before {
    content: ""; position: absolute; left: 0; right: 0; top: 15px; height: 2px; background: var(--gold);
  }
  .icon-rail ul {
    position: relative; list-style: none; display: flex; justify-content: center; gap: 30px;
  }
  .icon-rail li, .pin-badge {
    width: 26px; height: 26px; border-radius: 50%;
    background: var(--card-black); border: 2px solid var(--gold);
    display: flex; align-items: center; justify-content: center;
  }
  .icon-rail svg, .pin-badge svg { width: 13px; height: 13px; fill: none; stroke: var(--gold); stroke-width: 2; stroke-linecap: round; stroke-linejoin: round; }

  .contact-list {
    list-style: none; margin-top: 48px; text-align: center;
    color: var(--white); font-size: 13px; line-height: 23px; letter-spacing: 0.2px;
  }

  .address-rule {
    position: absolute; top: 412px; left: 0; right: 0; height: 7px;
    background: linear-gradient(90deg, var(--gold-deep), var(--gold-light), var(--gold-deep));
  }
  .pin-badge { position: absolute; top: 426px; left: 50%; transform: translateX(-50%); }
  .pin-badge::before, .pin-badge::after {
    content: ""; position: absolute; top: 11px; height: 2px; width: 152px; background: var(--gold);
  }
  .pin-badge::before { right: 26px; }
  .pin-badge::after { left: 26px; }

  .address {
    position: absolute; top: 466px; left: 0; right: 0; text-align: center;
    color: var(--gold); font-family: var(--serif); font-size: 13px; line-height: 19px; font-style: normal;
  }

  /* ---------- Back: brand side ---------- */
  .card-back .edge-top, .card-back .edge-bottom {
    position: absolute; left: 0; right: 0; height: 34px;
    background: linear-gradient(90deg, var(--gold-deep), var(--gold-light), var(--gold));
  }
  .card-back .edge-top { top: 0; clip-path: polygon(0 0, 100% 0, 100% 100%, 0 45%); }
  .card-back .edge-bottom { bottom: 0; clip-path: polygon(0 0, 100% 70%, 100% 100%, 0 100%); }

  .back-brand {
    position: absolute; top: 50%; left: 0; right: 0; transform: translateY(-50%);
    text-align: center; color: var(--gold); font-family: var(--serif); font-weight: 700;
  }
  .back-brand .dot {
    display: block; width: 40px; height: 40px; margin: 0 auto 14px; border-radius: 50%; background: var(--gold);
  }
  .back-brand .name-main { display: block; font-size: 28px; letter-spacing: 2px; line-height: 1.1; }
  .back-brand .name-sub { display: block; font-size: 13px; letter-spacing: 0.8px; margin-top: 4px; }
</style>
</head>
<body>
<main class="canvas">

  <article class="card card-front" aria-label="Clinician side">
    <div class="header-band">
      <svg viewBox="0 0 330 140" preserveAspectRatio="none" aria-hidden="true">
        <defs>
          <linearGradient id="band-gold" x1="0" x2="1" y1="0" y2="0">
            <stop offset="0" stop-color="#e9a51f"/>
            <stop offset="0.5" stop-color="#fcca45"/>
            <stop offset="1" stop-color="#f0ae25"/>
          </linearGradient>
        </defs>
        <path d="M0 0 H330 V100 Q165 150 0 100 Z" fill="url(#band-gold)"/>
      </svg>
    </div>

    <div class="brand-mark">
      <span class="dot"></span>
      <span class="name-main">MEADOWLARK</span>
      <span class="name-sub">BEHAVIORAL PARTNERS, LLC</span>
    </div>

    <header class="clinician">
      <h1 class="person">DANA R. WHITFIELD, LP</h1>
      <p class="role">President</p>
    </header>

    <section class="contact-panel">
      <div class="icon-rail">
        <ul>
          <li><svg viewBox="0 0 24 24"><path d="M5 3h4l2 5-3 2a11 11 0 0 0 6 6l2-3 5 2v4a2 2 0 0 1-2 2A17 17 0 0 1 3 5a2 2 0 0 1 2-2z"/></svg></li>
          <li><svg viewBox="0 0 24 24"><rect x="7" y="2" width="10" height="20" rx="2"/><path d="M11 18h2"/></svg></li>
          <li><svg viewBox="0 0 24 24"><rect x="3" y="5" width="18" height="14" rx="1"/><path d="M3 6l9 7 9-7"/></svg></li>
          <li><svg viewBox="0 0 24 24"><circle cx="12" cy="12" r="9"/><path d="M3 12h18M12 3c3 3 3 15 0 18M12 3c-3 3-3 15 0 18"/></svg></li>
        </ul>
      </div>
      <ul class="contact-list">
        <li>(316) 555-0142</li>
        <li>(316) 555-0142</li>
        <li>info@youremail.com</li>
        <li>www.yourwebsite.com</li>
      </ul>
    </section>

    <div class="address-rule"></div>
    <div class="pin-badge"><svg viewBox="0 0 24 24"><path d="M12 22s7-7 7-12a7 7 0 0 0-14 0c0 5 7 12 7 12z"/><circle cx="12" cy="10" r="2.5"/></svg></div>
    <address class="address">418 S. WILLOW ST.<br>Hutchinson, Kansas 67501</address>
  </article>

  <article class="card card-back" aria-label="Brand side">
    <div class="edge-top"></div>
    <div class="back-brand">
      <span class="dot"></span>
      <span class="name-main">MEADOWLARK</span>
      <span class="name-sub">BEHAVIORAL PARTNERS, LLC</span>
    </div>
    <div class="edge-bottom"></div>
  </article>

</main>
</body>
</html>
```